elec business card

hi all

Im after a new age looking business card with my company logo on it

must include these details, I would like the PH and Email to be symbols

If the colours used for card could be kept within the colours used in logo that I have supplied that would be great, if another colour is to be used dark grey would be ok. no light bulbs etc thanks

Details below to be incorporated on card

Dorian Pellow

Lic E781392

PH 0219467318

E info@brightwayelectrical.example.nz

Domestic Commercial Industrial Electricians

```html
<!DOCTYPE html>
<html lang="en">
<head>
<meta charset="utf-8">
<title>Brightway Electrical – Business Card</title>
<link rel="stylesheet" href="https://fonts.googleapis.com/css2?family=Poppins:wght@300;400;600;700&display=swap">
<style>
  :root {
    --stage: #e4e2e1;
    --card-white: #ffffff;
    --brand-blue: #1f6fb8;
    --panel-blue: #4399d5;
    --panel-black: #05070a;
    --label-blue: #4aa3e6;
    --white: #ffffff;
  }
  * { box-sizing: border-box; margin: 0; padding: 0; }
  html, body {
    width: 1200px; height: 900px; overflow: hidden;
    background: var(--stage);
    font-family: "Poppins", Arial, sans-serif;
  }
  .canvas { position: relative; width: 1200px; height: 900px; }

  .card {
    position: absolute;
    width: 525px; height: 300px;
    border-radius: 3px;
    overflow: hidden;
    box-shadow: 0 14px 30px rgba(0,0,0,0.18);
  }

  /* Front side */
  .card-front {
    left: 300px; top: 110px;
    background: var(--card-white);
    display: flex; align-items: center; justify-content: center;
  }
  .wordmark { text-align: right; line-height: 1; white-space: nowrap; }
  .wordmark-name {
    display: block;
    font-weight: 700; font-size: 54px; letter-spacing: 3px;
    color: var(--brand-blue);
  }
  .wordmark-sub {
    display: block; margin-top: 4px;
    font-weight: 700; font-size: 13px; letter-spacing: 6px;
    color: var(--brand-blue);
  }

  /* Back side */
  .card-back { left: 395px; top: 490px; background: var(--panel-black); }
  .back-split { position: absolute; inset: 0; }

  .holder {
    position: absolute; left: 30px; bottom: 62px;
    width: 190px;
    color: var(--white);
  }
  .holder-name { font-weight: 600; font-size: 23px; letter-spacing: 0.2px; white-space: nowrap; }
  .holder-trade {
    margin-top: 4px;
    font-weight: 300; font-size: 11px; line-height: 1.35;
  }

  .back-brand {
    position: absolute; right: 40px; top: 58px;
  }
  .back-brand .wordmark-name { color: var(--white); font-size: 32px; letter-spacing: 2px; }
  .back-brand .wordmark-sub { color: var(--white); font-size: 8px; letter-spacing: 4px; }

  .contact {
    position: absolute; left: 258px; top: 178px;
    list-style: none;
    font-size: 10px; line-height: 1.9;
    white-space: nowrap;
    color: var(--white);
  }
  .contact-label { color: var(--label-blue); font-weight: 400; }
  .contact-value { font-weight: 400; }
</style>
</head>
<body>
<main class="canvas">
  <section class="card card-front" aria-label="Business card front">
    <div class="wordmark">
      <span class="wordmark-name">BRIGHTWAY</span>
      <span class="wordmark-sub">ELECTRICAL</span>
    </div>
  </section>

  <section class="card card-back" aria-label="Business card back">
    <svg class="back-split" viewBox="0 0 525 300" preserveAspectRatio="none" aria-hidden="true">
      <polygon points="0,0 248,0 230,300 0,300" fill="var(--panel-blue)"/>
      <line x1="248" y1="0" x2="230" y2="300" stroke="var(--white)" stroke-width="6"/>
      <line x1="254" y1="0" x2="236" y2="300" stroke="var(--brand-blue)" stroke-width="5"/>
    </svg>

    <div class="holder">
      <p class="holder-name">Dorian Pellow</p>
      <p class="holder-trade">Domestic Commercial Industrial Electricians</p>
    </div>

    <div class="wordmark back-brand">
      <span class="wordmark-name">BRIGHTWAY</span>
      <span class="wordmark-sub">ELECTRICAL</span>
    </div>

    <ul class="contact">
      <li><span class="contact-label">License:</span> <span class="contact-value">E781392</span></li>
      <li><span class="contact-label">Phone:</span> <span class="contact-value">0219467318</span></li>
      <li><span class="contact-label">Email:</span> <span class="contact-value">info@brightwayelectrical.example.nz</span></li>
    </ul>
  </section>
</main>
</body>
</html>
```